RV BIZ CARDS

Hi,

Is it possible to see a one sided version (with logo and info) as well as a two-sided version (front side w/logo and back side with info)?
How do we choose card stock and finish once we approve a design?

We would like the following info included:

Marcus Trell
Trell Vantage Media
4157 Merrow Crescent, Suite 200
Los Angeles, CA 90068
(323) 555-0192
marcus@trellvantagemedia.example

```html
<!DOCTYPE html>
<html lang="en">
<head>
<meta charset="utf-8">
<title>Trell Vantage Media – Business Cards</title>
<link rel="stylesheet" href="https://fonts.googleapis.com/css2?family=Questrial&family=Poppins:wght@600&display=swap">
<style>
  :root {
    --backdrop: #2e2926;
    --card-light: #fbfbfa;
    --card-dark: #161616;
    --ink-dark: #1e1a18;
    --ink-light: #f2f2f2;
    --ink-muted: #cfcfcf;
    --rule: #8a8a8a;
  }
  * { box-sizing: border-box; margin: 0; padding: 0; }
  html, body {
    width: 1200px;
    height: 780px;
    overflow: hidden;
    background: var(--backdrop);
  }
  .canvas {
    position: relative;
    width: 1200px;
    height: 780px;
    display: flex;
    align-items: center;
    justify-content: center;
    gap: 60px;
  }
  .card {
    position: relative;
    width: 500px;
    height: 286px;
    border-radius: 3px;
    box-shadow: 0 14px 30px rgba(0,0,0,0.45);
  }
  /* Front */
  .card--front {
    background: var(--card-light);
    display: flex;
    flex-direction: column;
    align-items: center;
    justify-content: center;
    gap: 14px;
  }
  .brand-mark {
    width: 50px;
    height: 50px;
    border: 2px solid var(--ink-dark);
    border-radius: 50%;
  }
  .brand-name {
    font-family: "Questrial", sans-serif;
    font-size: 24px;
    letter-spacing: 0.14em;
    color: var(--ink-dark);
    text-transform: uppercase;
  }
  /* Back */
  .card--back {
    background: var(--card-dark);
    color: var(--ink-light);
    font-family: "Questrial", sans-serif;
  }
  .identity {
    position: absolute;
    right: 272px;
    top: 100px;
    text-align: right;
  }
  .identity__name {
    font-family: "Poppins", sans-serif;
    font-weight: 600;
    font-size: 13px;
    letter-spacing: 0.02em;
    text-transform: uppercase;
  }
  .identity__company {
    font-size: 12.5px;
    color: var(--ink-muted);
    margin-top: 1px;
  }
  .divider {
    position: absolute;
    left: 244px;
    top: 92px;
    width: 1px;
    height: 56px;
    background: var(--rule);
  }
  .contact {
    position: absolute;
    left: 258px;
    top: 102px;
    list-style: none;
    font-size: 13px;
    line-height: 1.6;
  }
  .contact__item {
    display: flex;
    align-items: center;
    gap: 6px;
  }
  .contact__icon { width: 14px; height: 14px; flex: none; }
  .address {
    position: absolute;
    left: 0;
    right: 0;
    top: 196px;
    text-align: center;
    font-size: 13.5px;
    letter-spacing: 0.02em;
  }
</style>
</head>
<body>
<main class="canvas">
  <section class="card card--front" aria-label="Card front">
    <div class="brand-mark" aria-hidden="true"></div>
    <div class="brand-name">Trell Vantage</div>
  </section>

  <section class="card card--back" aria-label="Card back">
    <div class="identity">
      <div class="identity__name">Marcus Trell</div>
      <div class="identity__company">Trell Vantage Media</div>
    </div>
    <div class="divider"></div>
    <ul class="contact">
      <li class="contact__item">
        <svg class="contact__icon" viewBox="0 0 14 14" aria-hidden="true">
          <circle cx="7" cy="7" r="6.3" fill="none" stroke="#f2f2f2" stroke-width="1"/>
          <rect x="4.6" y="3.3" width="4.8" height="7.4" rx="0.8" fill="none" stroke="#f2f2f2" stroke-width="1"/>
        </svg>
        <span>(323) 555-0192</span>
      </li>
      <li class="contact__item">
        <svg class="contact__icon" viewBox="0 0 14 14" aria-hidden="true">
          <circle cx="7" cy="7" r="6.5" fill="#f2f2f2"/>
          <rect x="3.6" y="4.8" width="6.8" height="4.6" fill="#161616"/>
          <path d="M3.8 5 L7 7.6 L10.2 5" fill="none" stroke="#f2f2f2" stroke-width="0.8"/>
        </svg>
        <span>marcus@trellvantagemedia.example</span>
      </li>
    </ul>
    <p class="address">4157 Merrow Crescent, Suite 200, Los Angeles, CA 90068</p>
  </section>
</main>
</body>
</html>
```